Business Cards for a small business advisory (business services)

Professional look. Same as would apply for a lawyer, accountant, or other financial services professional. Please use the logo colors

Target Market(s)

small business owners

Industry/Entity Type

Financial Servics

Contact Information for Business Card

Name: Gavin L. Whitmore, CAIA / Title: Business Advisor / Office #: (718) 294-7716 / Mobile #: (917) 382-5047 / Email: g.whitmore@clearfieldventurepartners.example / Web: www.clearfieldventurepartners.example

Font styles to use
Sans Serif

```html
<!DOCTYPE html>
<html lang="en">
<head>
<meta charset="utf-8">
<title>Clearfield Venture Partners – Business Cards</title>
<link rel="stylesheet" href="https://fonts.googleapis.com/css2?family=Poppins:wght@400;600&display=swap">
<style>
  :root {
    --navy: #1b3869;
    --green: #8cc63f;
    --ink: #2b2b33;
    --paper: #ffffff;
    --backdrop: #9b9b9b;
  }
  * { margin: 0; padding: 0; box-sizing: border-box; }
  html, body { width: 1093px; height: 1200px; overflow: hidden; }
  body {
    background: var(--backdrop);
    font-family: "Poppins", Arial, sans-serif;
    position: relative;
  }
  .card {
    position: absolute;
    left: 264px;
    width: 580px;
    height: 357px;
    overflow: hidden;
  }
  .card--front { top: 226px; background: var(--paper); }
  .card--back { top: 620px; background: var(--navy); }

  .name-accent {
    position: absolute; left: 0; top: 53px;
    width: 18px; height: 43px; background: var(--green);
  }
  .name {
    position: absolute; left: 27px; top: 50px;
    font-weight: 600; font-size: 22px; letter-spacing: -0.3px;
    color: var(--navy); line-height: 1.2;
  }
  .name .credential { color: var(--green); }
  .title {
    position: absolute; left: 27px; top: 76px;
    font-size: 17px; color: var(--ink);
  }
  .edge-rule {
    position: absolute; right: 4px; top: 0; bottom: 0;
    width: 4px; background: var(--navy);
  }
  .contacts {
    position: absolute; left: 27px; top: 234px;
    list-style: none;
  }
  .contacts li {
    display: flex; align-items: center; gap: 7px;
    height: 24px; font-size: 17px; color: var(--ink);
    white-space: nowrap;
  }
  .contacts svg { width: 17px; height: 17px; flex: none; fill: var(--navy); }

  .brand {
    position: absolute; left: 0; right: 0; top: 148px;
    display: flex; align-items: center; justify-content: center; gap: 14px;
  }
  .brand-dot { width: 34px; height: 34px; border-radius: 50%; background: var(--green); }
  .brand-name {
    font-weight: 600; font-size: 34px; color: var(--paper); letter-spacing: 0.2px;
    white-space: nowrap;
  }
  .tagline {
    position: absolute; left: 0; right: 0; top: 204px;
    text-align: center; font-weight: 600; font-size: 8.5px;
    letter-spacing: 0.3px; color: var(--paper);
    text-transform: uppercase;
  }
</style>
</head>
<body>
  <section class="card card--front">
    <div class="name-accent"></div>
    <h1 class="name">GAVIN L. WHITMORE, <span class="credential">CAIA</span></h1>
    <p class="title">Business Advisor</p>
    <div class="edge-rule"></div>
    <ul class="contacts">
      <li>
        <svg viewBox="0 0 24 24" aria-hidden="true"><path d="M6.6 10.8a15.1 15.1 0 0 0 6.6 6.6l2.2-2.2c.3-.3.7-.4 1-.2 1.1.4 2.3.6 3.6.6.6 0 1 .4 1 1V20c0 .6-.4 1-1 1A17 17 0 0 1 3 4c0-.6.4-1 1-1h3.5c.6 0 1 .4 1 1 0 1.3.2 2.5.6 3.6.1.3 0 .7-.2 1l-2.3 2.2z"/></svg>
        (718) 294-7716
      </li>
      <li>
        <svg viewBox="0 0 24 24" aria-hidden="true"><path d="M7 1h10a2 2 0 0 1 2 2v18a2 2 0 0 1-2 2H7a2 2 0 0 1-2-2V3a2 2 0 0 1 2-2zm0 3v14h10V4H7zm5 15.5a1 1 0 1 0 0 2 1 1 0 0 0 0-2z"/></svg>
        (917) 382-5047
      </li>
      <li>
        <svg viewBox="0 0 24 24" aria-hidden="true"><path d="M2 5h20v14H2V5zm2 2v.5l8 5.5 8-5.5V7L12 12.3 4 7z"/></svg>
        g.whitmore@clearfieldventurepartners.example
      </li>
      <li>
        <svg viewBox="0 0 24 24" aria-hidden="true"><path d="M12 2a10 10 0 1 0 0 20 10 10 0 0 0 0-20zm6.9 6h-3a15 15 0 0 0-1.3-3.9A8 8 0 0 1 18.9 8zM12 4c.8 1.2 1.5 2.5 1.9 4h-3.8c.4-1.5 1.1-2.8 1.9-4zM4.3 14a8 8 0 0 1 0-4h3.4a16 16 0 0 0 0 4H4.3zm.8 2h3a15 15 0 0 0 1.3 3.9A8 8 0 0 1 5.1 16zm3-8h-3a8 8 0 0 1 4.3-3.9C8.8 5.3 8.4 6.6 8.1 8zM12 20c-.8-1.2-1.5-2.5-1.9-4h3.8c-.4 1.5-1.1 2.8-1.9 4zm2.3-6H9.7a14 14 0 0 1 0-4h4.6a14 14 0 0 1 0 4zm.3 5.9c.6-1.2 1-2.5 1.3-3.9h3a8 8 0 0 1-4.3 3.9zm1.7-5.9a16 16 0 0 0 0-4h3.4a8 8 0 0 1 0 4h-3.4z"/></svg>
        www.clearfieldventurepartners.example
      </li>
    </ul>
  </section>

  <section class="card card--back">
    <div class="brand">
      <span class="brand-dot" aria-hidden="true"></span>
      <span class="brand-name">Clearfield Venture Partners</span>
    </div>
    <p class="tagline">Clear advice for owners planning their next business move</p>
  </section>
</body>
</html>
```